Educational clinic needs a new webpage design

I have a relatively new website but I am unhappy with the design. I was hoping the look of it would more match my logo, brochures, business cards, and postcards. The content is good and it's already mobile ready. The designer used square space, which I would like to keep if possible. My website is www.willowgatestudio.com

Target Market(s)

Parents of school age children

Industry/Entity Type

Education

Number of Pages Required

5+ page

Requirements
Must have
• Pictures must depict the diversity of our students. We service all ages, from preschool through college and our students come from varying races.
Should not have
• I try to avoid the word "tutoring" because what we do is so much more. I like the tag line of "results that go beyond traditional tutoring"

```html
<!DOCTYPE html>
<html lang="en">
<head>
<meta charset="utf-8">
<title>Willowgate Learning Studio</title>
<link rel="stylesheet" href="https://fonts.googleapis.com/css2?family=Arimo:wght@400;700&family=Mulish:wght@300;400;600;700&display=swap">
<style>
:root{
  --purple:#6b2c8f;
  --purple-soft:#8a4bb0;
  --green:#8cc63f;
  --green-band:#7fb33a;
  --ink:#555;
  --muted:#777;
  --grey-band:#efefef;
  --night:#231133;
  --bar:#1c1c1c;
  --white:#fff;
}
*{box-sizing:border-box;margin:0;padding:0}
html,body{width:680px;height:1200px;overflow:hidden}
body{font-family:"Mulish",sans-serif;color:var(--ink);background:var(--white);position:relative}
.wrap{position:absolute;left:88px;right:88px}

/* header */
.site-header{position:absolute;top:0;left:0;width:680px;height:59px;background:var(--white)}
.brand{position:absolute;left:88px;top:14px;display:flex;align-items:center;gap:8px}
.brand-mark{width:26px;height:26px;border-radius:50%;background:var(--purple)}
.brand-name{font-family:"Arimo",sans-serif;font-weight:700;font-size:15px;color:var(--purple);line-height:1.05;letter-spacing:.3px}
.main-nav{position:absolute;right:88px;top:0;display:flex;height:50px}
.main-nav a{font-size:8px;letter-spacing:.5px;color:var(--purple);text-decoration:none;padding:0 7px;display:flex;align-items:center}
.main-nav a.is-active{background:var(--purple);color:var(--white);padding:0 9px}

/* hero */
.hero{position:absolute;top:59px;left:0;width:680px;height:305px;
  background:linear-gradient(180deg,#e9eef2 0%,#c9d3dc 45%,#9fb0c0 70%,#f2ece0 100%)}
.hero-caption{position:absolute;left:0;top:150px;width:340px;height:112px;background:rgba(50,50,50,.78);padding:10px 0 0 88px}
.hero-title{font-family:"Arimo",sans-serif;font-weight:700;font-size:20.5px;line-height:25px;color:var(--white)}
.btn{display:inline-block;background:var(--purple);color:var(--white);font-family:"Arimo",sans-serif;font-weight:700;font-size:9px;letter-spacing:.9px;text-transform:uppercase;padding:5px 17px}
.hero .btn{position:absolute;left:233px;top:86px}

/* intro band */
.intro{position:absolute;top:364px;left:0;width:680px;height:106px;background:linear-gradient(120deg,var(--green-band),#8dc043 55%,#78aa34)}
.intro-text{position:absolute;left:88px;top:12px;width:520px;font-weight:300;font-size:19px;line-height:28px;color:var(--white)}
.intro .btn{position:absolute;right:88px;top:74px}

/* programs */
.programs-title{position:absolute;top:508px;left:0;width:680px;text-align:center;font-weight:300;font-size:21px;color:var(--ink);letter-spacing:.3px}
.program-list{position:absolute;top:558px;left:88px;display:flex;gap:21px}
.program-card{width:154px;height:207px;border:1px solid var(--purple-soft);text-align:center;padding-top:13px;position:relative}
.program-icon{width:66px;height:66px;border-radius:50%;background:var(--purple);margin:0 auto;display:block}
.program-name{font-weight:700;font-size:8px;color:var(--green);margin-top:13px;letter-spacing:.2px}
.program-text{font-size:7px;line-height:10.5px;color:var(--muted);padding:0 11px;margin-top:9px}
.program-card .btn{position:absolute;left:34px;bottom:12px;font-size:8px;padding:5px 18px}

/* subscribe */
.newsletter{position:absolute;top:812px;left:0;width:680px;height:128px;background:var(--grey-band)}
.newsletter-title{position:absolute;top:37px;width:680px;text-align:center;font-size:16.5px;font-weight:300;color:#444}
.newsletter-title strong{font-weight:600}
.newsletter-field{position:absolute;left:123px;top:77px;width:316px;height:24px;background:var(--white);border:1px solid #aaa;border-radius:2px}
.newsletter-btn{position:absolute;left:446px;top:77px;width:110px;height:24px;background:var(--green);color:var(--white);font-family:"Arimo",sans-serif;font-weight:700;font-size:10px;letter-spacing:1.5px;display:flex;align-items:center;justify-content:center;border-radius:2px}

/* footer */
.site-footer{position:absolute;top:940px;left:0;width:680px;height:236px;background:var(--night);color:var(--white)}
.footer-brand{position:absolute;left:88px;top:30px;display:flex;align-items:center;gap:7px}
.footer-brand .brand-mark{width:22px;height:22px;background:var(--white)}
.footer-brand .brand-name{color:var(--white);font-size:12px}
.footer-divider{position:absolute;left:272px;top:30px;width:1px;height:186px;background:#7a6a88}
.footer-label{font-family:"Arimo",sans-serif;font-weight:700;font-size:7.5px;letter-spacing:.4px;position:absolute}
.contact-list{position:absolute;left:88px;top:106px;list-style:none}
.contact-list li{display:flex;align-items:center;gap:12px;height:19px;margin-bottom:7.5px;font-size:7.5px;color:var(--purple-soft)}
.contact-list svg{width:19px;height:19px;flex:none}
.footer-heading{position:absolute;left:293px;top:40px;font-weight:300;font-size:17px;letter-spacing:1px}
.field-line{position:absolute;border-bottom:1px solid var(--purple-soft);font-size:7px;color:var(--purple-soft);padding-bottom:2px}
.send-btn{position:absolute;left:522px;top:178px;width:70px;height:15px;background:var(--green);font-family:"Arimo",sans-serif;font-weight:700;font-size:7.5px;letter-spacing:1px;display:flex;align-items:center;justify-content:center}
.copyright{position:absolute;top:1176px;left:0;width:680px;height:24px;background:var(--bar);color:#666;font-size:6px;display:flex;align-items:center;justify-content:center}
</style>
</head>
<body>

<header class="site-header">
  <div class="brand">
    <span class="brand-mark"></span>
    <span class="brand-name">WILLOWGATE<br>Learning Studio</span>
  </div>
  <nav class="main-nav">
    <a class="is-active" href="#">HOME</a>
    <a href="#">SERVICES</a>
    <a href="#">ABOUT US</a>
    <a href="#">PAYMENTS</a>
    <a href="#">CONTACT US</a>
  </nav>
</header>

<section class="hero" role="img" aria-label="Photo of four smiling students of different backgrounds lying on the floor with open books">
  <div class="hero-caption">
    <h1 class="hero-title">RESULTS THAT GO<br>BEYOND TRADITIONAL<br>TUTORING</h1>
    <a class="btn" href="#">Learn More</a>
  </div>
</section>

<section class="intro">
  <p class="intro-text">We offer tutoring and learning programs for students of all ages and learning types.</p>
  <a class="btn" href="#">Read More</a>
</section>

<h2 class="programs-title">SPECIALTY PROGRAMS</h2>
<div class="program-list">
  <article class="program-card">
    <svg class="program-icon" viewBox="0 0 66 66" aria-hidden="true">
      <circle cx="33" cy="33" r="33" fill="#6b2c8f"/>
      <g fill="none" stroke="#fff" stroke-width="2" stroke-linecap="round">
        <path d="M27 41c0-5-5-7-5-13a11 11 0 0 1 22 0c0 6-5 8-5 13z"/>
        <line x1="28" y1="45" x2="38" y2="45"/><line x1="29" y1="49" x2="37" y2="49"/>
        <line x1="33" y1="10" x2="33" y2="13"/><line x1="18" y1="16" x2="20" y2="18"/><line x1="48" y1="16" x2="46" y2="18"/>
        <line x1="13" y1="28" x2="16" y2="28"/><line x1="50" y1="28" x2="53" y2="28"/>
      </g>
    </svg>
    <h3 class="program-name">FOCUS</h3>
    <p class="program-text">The FOCUS program is a cognitive brain training program based on proven ideas from the fields of behavioral optometry and cognitive neuroscience. It consists of a number of brain...</p>
    <a class="btn" href="#">Read More</a>
  </article>
  <article class="program-card">
    <svg class="program-icon" viewBox="0 0 66 66" aria-hidden="true">
      <circle cx="33" cy="33" r="33" fill="#6b2c8f"/>
      <circle cx="33" cy="20" r="7" fill="#fff"/>
      <path d="M20 50V34q13-7 26 0v16q-13-5-26 0z" fill="#fff"/>
      <line x1="33" y1="31" x2="33" y2="48" stroke="#6b2c8f" stroke-width="2"/>
    </svg>
    <h3 class="program-name">BRIGHT PATH READING PROGRAM</h3>
    <p class="program-text">This program teaches reading and spelling skills from the ground up. Students of all ages who are struggling with reading can benefit from this program. In addition to promoting...</p>
    <a class="btn" href="#">Read More</a>
  </article>
  <article class="program-card">
    <svg class="program-icon" viewBox="0 0 66 66" aria-hidden="true">
      <circle cx="33" cy="33" r="33" fill="#6b2c8f"/>
      <g fill="none" stroke="#fff" stroke-width="2.2" stroke-linecap="round" stroke-linejoin="round">
        <path d="M20 28a9 9 0 0 1 18 0c0 6-7 7-7 13a4 4 0 0 1-8 0"/>
        <path d="M25 29a4 4 0 0 1 8 0c0 3-4 3-4 6"/>
        <path d="M38 33h4l2-6 3 12 3-9 2 3h3"/>
      </g>
    </svg>
    <h3 class="program-name">CLEAR LISTENING EARS</h3>
    <p class="program-text">People of all ages can benefit from the Listening Ears training and exercises, including students with attention deficit disorder, dyslexia, learning disability, communication and emotional...</p>
    <a class="btn" href="#">Read More</a>
  </article>
</div>

<section class="newsletter">
  <h2 class="newsletter-title"><strong>STAY UPDATED</strong> WITH LATEST NEWS AND OTHER STUFF</h2>
  <div class="newsletter-field"></div>
  <div class="newsletter-btn">SUBSCRIBE</div>
</section>

<footer class="site-footer">
  <div class="footer-brand">
    <span class="brand-mark"></span>
    <span class="brand-name">WILLOWGATE<br>Learning Studio</span>
  </div>
  <span class="footer-label" style="left:88px;top:77px">CONTACT DETAILS</span>
  <ul class="contact-list">
    <li><svg viewBox="0 0 20 20"><circle cx="10" cy="10" r="9" fill="none" stroke="#8a4bb0"/><path d="M10 15s-3.5-3.8-3.5-6.2a3.5 3.5 0 0 1 7 0C13.5 11.2 10 15 10 15z" fill="none" stroke="#8a4bb0"/><circle cx="10" cy="8.8" r="1.2" fill="#8a4bb0"/></svg>418 Alder Row, BROOKFIELD, IL</li>
    <li><svg viewBox="0 0 20 20"><circle cx="10" cy="10" r="9" fill="none" stroke="#8a4bb0"/><path d="M7 5.5l2 2.2-1 1.3a6 6 0 0 0 3 3l1.3-1 2.2 2-1.2 1.5C10 14.5 5.5 10 5.5 6.7z" fill="#8a4bb0"/></svg>555-238-0194</li>
    <li><svg viewBox="0 0 20 20"><circle cx="10" cy="10" r="9" fill="none" stroke="#8a4bb0"/><rect x="5.5" y="7" width="9" height="6.5" fill="#8a4bb0"/><path d="M5.5 7l4.5 3.5L14.5 7" fill="none" stroke="#231133"/></svg>info@willowgatestudio.com</li>
    <li><svg viewBox="0 0 20 20"><circle cx="10" cy="10" r="9" fill="none" stroke="#8a4bb0"/><circle cx="10" cy="10" r="3" fill="#8a4bb0"/></svg>willowgatestudio.com/community</li>
  </ul>
  <div class="footer-divider"></div>
  <h2 class="footer-heading">KEEP IN TOUCH</h2>
  <span class="footer-label" style="left:294px;top:96px">CONTACT FORM</span>
  <div class="field-line" style="left:294px;top:120px;width:141px">Name*</div>
  <div class="field-line" style="left:452px;top:120px;width:140px">Email*</div>
  <div class="field-line" style="left:294px;top:162px;width:298px">Message</div>
  <div class="send-btn">SEND</div>
</footer>

<div class="copyright">Copyright 2016 &nbsp;|&nbsp; Willowgate Learning Studio &nbsp;|&nbsp; All Rights Reserved.</div>

</body>
</html>
```